Corvimo Business Card

Corvimo is a young and energetic software development consultancy. We spend our time on the road working with clients on their sites an meeting new potential customers and employees!

We need a sharp, vibrant and memorable business card that will inspires those that receive it to look after it as it oozes quality and is a nice thing in its own right.

We like bold colours and distinctive design. So show us what you can do.

In terms of information on the card, it would be good to see:

* Our logo (Obviously :) )
* Employee name
* Email
* Website address
* Mobile number
* Full company name (Corvimo ltd)
* Registered company number
* Registered company address

Industry/Entity Type

Software

Requirements
Nice to have
• We are thinking that having a QR Code on the business card could be a good way of adding active marketing. It would be good to see if you are able to merge the kind of element in to your designs!

Maybe something special could be achieved using a visual QR Code like those produced at http://www.pixoranta.example/ ? You have our media so feel free to have a play.

```html
<!DOCTYPE html>
<html lang="en">
<head>
<meta charset="utf-8">
<title>Corvimo Business Card</title>
<link rel="stylesheet" href="https://fonts.googleapis.com/css2?family=Rajdhani:wght@400;600&display=swap">
<style>
  :root {
    --brand-red: #c41e2f;
    --paper: #ffffff;
    --backdrop: #a9abae;
    --ink-light: #ffffff;
  }
  * { box-sizing: border-box; margin: 0; padding: 0; }
  html, body {
    width: 1200px; height: 900px; overflow: hidden;
    background: var(--backdrop);
    font-family: "Rajdhani", sans-serif;
  }
  .canvas {
    position: relative; width: 1200px; height: 900px;
  }
  .card {
    position: absolute; left: 320px;
    width: 560px; height: 320px;
    overflow: hidden;
    box-shadow: 0 4px 12px rgba(0,0,0,0.18);
  }
  /* Back of card */
  .card-back { top: 100px; background: var(--brand-red); }
  .card-back .name-band {
    position: absolute; left: 0; top: 0; bottom: 0; width: 78px;
    background: var(--paper);
    display: flex; align-items: center; justify-content: center;
  }
  .card-back .name-band .wordmark {
    transform: rotate(-90deg);
    white-space: nowrap;
    font-size: 62px; font-weight: 600; letter-spacing: 1px;
    color: var(--brand-red);
  }
  .card-back .band-rule {
    position: absolute; top: 0; bottom: 0; left: 84px; width: 2px;
    background: var(--paper);
  }
  .card-back .pattern-field {
    position: absolute; left: 92px; right: 0; top: 0; bottom: 0;
    background: var(--brand-red);
  }
  /* Front of card */
  .card-front { top: 480px; background: var(--paper); }
  .card-front .logo-area {
    position: absolute; left: 0; top: 0; bottom: 0; width: 272px;
    display: flex; align-items: center; justify-content: center;
  }
  .card-front .wordmark {
    font-size: 58px; font-weight: 600; letter-spacing: 1px;
    color: var(--brand-red);
  }
  .card-front .details {
    position: absolute; left: 272px; top: 0; right: 0; bottom: 0;
    background: var(--brand-red);
    color: var(--ink-light);
    padding: 42px 20px 0 30px;
    text-transform: uppercase;
  }
  .card-front .details::before {
    content: ""; position: absolute; left: 8px; top: 0; bottom: 0;
    width: 2px; background: var(--paper);
  }
  .person-name { font-size: 19px; font-weight: 400; letter-spacing: 1px; }
  .person-role { font-size: 11px; letter-spacing: 1px; margin-bottom: 18px; }
  .contact-list { list-style: none; font-size: 12px; letter-spacing: 0.5px; line-height: 1.35; margin-bottom: 16px; }
  .contact-list li { display: flex; align-items: center; gap: 6px; }
  .contact-list svg { width: 10px; height: 10px; flex: none; }
  .company-name { font-size: 12px; font-weight: 600; letter-spacing: 0.5px; }
  .company-address { font-size: 12px; line-height: 1.25; letter-spacing: 0.5px; }
</style>
</head>
<body>
<main class="canvas">
  <section class="card card-back" aria-label="Card back">
    <div class="name-band"><span class="wordmark">CORVIMO</span></div>
    <div class="band-rule"></div>
    <div class="pattern-field" role="img" aria-label="Repeating brand name pattern in white on red"></div>
  </section>

  <section class="card card-front" aria-label="Card front">
    <div class="logo-area"><span class="wordmark">CORVIMO</span></div>
    <div class="details">
      <p class="person-name">Elias Brandt</p>
      <p class="person-role">Consultant</p>
      <ul class="contact-list">
        <li>
          <svg viewBox="0 0 10 10" aria-hidden="true"><rect x="2.5" y="0.5" width="5" height="9" rx="1" fill="none" stroke="#fff"/><circle cx="5" cy="8" r="0.6" fill="#fff"/></svg>
          +47 900 00 000
        </li>
        <li>
          <svg viewBox="0 0 10 10" aria-hidden="true"><rect x="0.5" y="2" width="9" height="6" fill="#fff"/><path d="M0.5 2 L5 5.5 L9.5 2" fill="none" stroke="#c41e2f" stroke-width="0.8"/></svg>
          brandt@corvimosoft.example
        </li>
        <li>
          <svg viewBox="0 0 10 10" aria-hidden="true"><circle cx="5" cy="5" r="4.3" fill="none" stroke="#fff"/><ellipse cx="5" cy="5" rx="1.8" ry="4.3" fill="none" stroke="#fff" stroke-width="0.7"/><line x1="0.7" y1="5" x2="9.3" y2="5" stroke="#fff" stroke-width="0.7"/></svg>
          www.corvimosoft.example
        </li>
      </ul>
      <p class="company-name">Corvimo ltd</p>
      <p class="company-address">Harbour address at, PO Box 00,<br>0000 Bergen,<br>Norway</p>
    </div>
  </section>
</main>
</body>
</html>
```